KRT,LLC

I need a flyer that has my company Logo on it as well as my book cover on it. I need for the flyer to read: "Ashes Under the Bridge" ~ A story of Money,Murder,Sex and family ties in the heart of the city. Read along as Curtis J. Hollow masterfully paint this Wilmington,Delaware tale like no other~The "T.K.V boys" clash in a rain of bullets against North sides own "Zinga boys."
At $14.99 you can own your own copy of "Ashes Under the Bridge."
Contact Curt Hollow @ 302-555-0147 to purchase your paper back copy.
OR
Visit:www.krtllcbooks.example
www.ashezunderthebridge.example
ashesunderthebridge24@mailbox.example
To purchase your order directly off line.
We accept paxo,CoinLeaf and debit cards for those individuals who wish to order on-line!

```html
<!DOCTYPE html>
<html lang="en">
<head>
<meta charset="utf-8">
<title>Ashes Under the Bridge — Flyer</title>
<link href="https://fonts.googleapis.com/css2?family=Archivo:wght@800&family=Barlow+Semi+Condensed:wght@600;700&family=Libre+Baskerville:wght@700&display=swap" rel="stylesheet">
<style>
  :root {
    --page: #ffffff;
    --ink: #000000;
    --red: #e31b23;
    --red-dark: #5a0a0c;
    --red-mid: #b3171c;
    --white: #ffffff;
    --cover-blue: #2b3493;
    --cover-navy: #151a3a;
  }
  * { margin: 0; padding: 0; box-sizing: border-box; }
  html, body { width: 1000px; height: 1200px; overflow: hidden; background: var(--page); }
  .flyer {
    position: absolute; left: 94px; top: 27px;
    width: 812px; height: 1148px;
    background: var(--ink);
    overflow: hidden;
    font-family: "Barlow Semi Condensed", "Arial Narrow", sans-serif;
    color: var(--white);
  }
  .hero-photo {
    position: absolute; left: 0; top: 0; width: 812px; height: 621px;
    background:
      radial-gradient(ellipse at 55% 35%, #e0413f 0%, #b3171c 35%, transparent 70%),
      radial-gradient(ellipse at 20% 80%, #c9302c 0%, transparent 55%),
      linear-gradient(160deg, #3a0506 0%, var(--red-mid) 45%, var(--red-dark) 100%);
  }
  .hero-art { position: absolute; left: 0; top: 0; width: 812px; height: 621px; }
  .band-title { font-family: "Archivo", Arial, sans-serif; font-weight: 800; fill: var(--white); }
  .price-text { font-family: "Barlow Semi Condensed", sans-serif; font-weight: 700; fill: var(--white); }
  .pitch {
    position: absolute; left: 48px; top: 650px; width: 600px;
    font-size: 20.5px; line-height: 25px; font-weight: 700;
  }
  .pitch-title { font-size: 31px; line-height: 34px; }
  .pitch-lead { font-size: 18px; }
  .details {
    position: absolute; left: 48px; top: 793px; width: 500px;
    font-size: 14.5px; line-height: 22px; font-weight: 700;
  }
  .details p { margin-bottom: 14px; }
  .details .links { margin-bottom: 16px; }
  .details .links span { display: block; color: var(--red); }
  .details .payment { width: 370px; line-height: 18px; }
  .brand-mark {
    position: absolute; left: 50px; top: 1024px; width: 64px; height: 64px;
    border: 2px solid var(--white); border-radius: 50%;
    display: flex; align-items: center; justify-content: center;
    font-size: 17px; font-weight: 700; color: var(--white);
  }
  .book-cover {
    position: absolute; left: 562px; top: 793px; width: 210px; height: 315px;
    background: linear-gradient(180deg, var(--cover-navy) 0%, var(--cover-navy) 45%, var(--cover-blue) 72%, var(--cover-blue) 100%);
  }
  .cover-photo {
    height: 145px;
    background: linear-gradient(180deg, #b9c3cc 0%, #9a7466 45%, #7a6b55 75%, #5f7a45 100%);
    border-bottom: 4px solid var(--red);
  }
  .cover-title {
    margin-top: 36px; text-align: center;
    font-family: "Libre Baskerville", Georgia, serif; font-weight: 700;
    font-size: 9px; letter-spacing: 0.5px; color: var(--red);
  }
  .cover-author {
    position: absolute; bottom: 18px; width: 100%; text-align: center;
    font-family: "Libre Baskerville", Georgia, serif; font-weight: 700;
    font-size: 5.5px; letter-spacing: 1px; color: var(--red);
  }
</style>
</head>
<body>
<main class="flyer">
  <div class="hero-photo" role="img" aria-label="Close-up photo of stacked rolls of cash tinted red"></div>
  <svg class="hero-art" viewBox="0 0 812 621">
    <polygon points="0,230 812,150 812,240 0,322" fill="var(--red)"/>
    <text class="band-title" x="400" y="262" font-size="68" text-anchor="middle" transform="rotate(-5.6 400 240)">Ashes Under</text>
    <polygon points="0,343 812,418 812,494 0,420" fill="var(--red)"/>
    <text class="band-title" x="400" y="442" font-size="66" text-anchor="middle" transform="rotate(5.3 400 420)">the Bridge</text>
    <circle cx="711" cy="585" r="70" fill="var(--red)"/>
    <circle cx="711" cy="585" r="72" fill="none" stroke="var(--red)" stroke-width="6" stroke-dasharray="3.2 3.2"/>
    <text class="price-text" x="711" y="570" font-size="34" text-anchor="middle">NOW</text>
    <text class="price-text" x="711" y="612" font-size="40" text-anchor="middle">$14.99</text>
  </svg>

  <section class="pitch">
    <span class="pitch-title">"Ashes Under the Bridge"</span>
    <span class="pitch-lead"> ~ A story of</span>
    Money,Murder,Sex and family ties in the heart of the city. Read along as Curtis J. Hollow masterfully paint this Wilmington,Delaware tale like no other~The "T.K.V boys" clash in a rain of bullets against North sides own "Zinga boys."
  </section>

  <section class="details">
    <p>At $14.99 you can own your own copy of "Ashes Under the Bridge."</p>
    <div class="links">
      Contact Curt Hollow @ 302-555-0147 to purchase your paper back copy. OR
      <span>Visit:www.krtllcbooks.example</span>
      <span>www.ashezunderthebridge.example</span>
      <span>ashesunderthebridge24@mailbox.example</span>
      To purchase your order directly off line.
    </div>
    <p class="payment">We accept paxo, CoinLeaf and debit cards for those individuals who wish to order on-line!</p>
  </section>

  <div class="brand-mark">KRT</div>

  <figure class="book-cover">
    <div class="cover-photo" role="img" aria-label="Cover photo of the author standing outside brick row houses"></div>
    <div class="cover-title">ASHES UNDER THE BRIDGE</div>
    <div class="cover-author">WRITTEN BY CURTIS J. HOLLOW</div>
  </figure>
</main>
</body>
</html>
```